Bluefinch Painting needs a Website

We need a website built for a Painting company I own, we mainly do residential painting, but don't want to be limited to that.

Need to have estimate request form.
Need pic's of past projects

I like the look of the website for http://www.harborline-painters.example
& "Thistledown Property inspections"

My logo that was designed here on ArtHive on the front page

I would like one of the houses I downloaded as part of the background
of the front page.

Target Market(s)

Home owners

Industry/Entity Type

Painting

Number of Pages Required

1 page

Font styles to use
Serif

Requirements
Must have
• Estimate request form for home owners to fill out -
• Name:
• Phone Number:
• Address:
• E-mail:
• Painting project description:
• And my info to:
• My phone number: (555) 318-7764
• My web address bluefinchpainting.example
Nice to have
• My logo that was designed here on ArtHive

```html
<!DOCTYPE html>
<html lang="en">
<head>
<meta charset="utf-8">
<title>Bluefinch Painting</title>
<link rel="stylesheet" href="https://fonts.googleapis.com/css2?family=Oswald:wght@400;500&family=Open+Sans:wght@400;600;700&family=Oxygen:wght@400;700&display=swap">
<style>
  :root {
    --header-blue: #1877c0;
    --page-blue: #13649d;
    --panel-navy: #0b2658;
    --field-border: #1b7ccb;
    --field-text: #3f86c4;
    --hero-shade: #3a3f3d;
    --hero-tone: #6f7a74;
    --white: #ffffff;
    --rule: #c8dcef;
  }
  * { margin: 0; padding: 0; box-sizing: border-box; }
  html, body { width: 1080px; height: 1200px; overflow: hidden; }
  body {
    position: relative;
    background: var(--page-blue);
    font-family: "Open Sans", Arial, sans-serif;
    color: var(--white);
  }
  .site-header {
    position: absolute; left: 0; top: 0; width: 1080px; height: 77px;
    background: var(--header-blue);
  }
  .brand {
    position: absolute; left: 146px; top: 22px;
    display: flex; align-items: center; gap: 10px;
    font-family: "Oswald", sans-serif; font-weight: 500;
    font-size: 24px; letter-spacing: 2px; text-transform: uppercase;
  }
  .brand-mark { width: 22px; height: 22px; background: var(--white); }
  .main-nav { position: absolute; top: 26px; left: 616px; display: flex; gap: 16px; }
  .main-nav a {
    display: block; height: 29px; line-height: 29px; padding: 0 9px;
    color: var(--white); text-decoration: none; font-weight: 600; font-size: 15.5px;
  }
  .main-nav a.is-active { background: var(--white); color: var(--header-blue); font-weight: 400; }
  .hero {
    position: absolute; left: 0; top: 77px; width: 1080px; height: 445px;
    background: linear-gradient(180deg, #5d6a72 0%, var(--hero-tone) 35%, #555c57 65%, var(--hero-shade) 100%);
  }
  .hero-title {
    position: absolute; left: 0; width: 1080px; top: 142px; text-align: center;
    font-family: "Oswald", sans-serif; font-weight: 500; font-size: 35px;
  }
  .hero-lead {
    position: absolute; left: 168px; width: 744px; top: 188px; text-align: center;
    font-size: 16px; line-height: 19px;
  }
  .hero-scroll { position: absolute; left: 528px; top: 338px; }
  .section-title {
    position: absolute; left: 0; width: 1080px; top: 530px; text-align: center;
    font-family: "Oswald", sans-serif; font-weight: 500; font-size: 35px;
  }
  .section-rule { position: absolute; left: 397px; top: 574px; width: 285px; height: 2px; background: var(--rule); }
  .about-photo {
    position: absolute; left: 151px; top: 595px; width: 256px; height: 179px;
    background: linear-gradient(180deg, #7f93a6 0%, #c9d0d3 45%, #e9ecec 70%, #51564f 100%);
  }
  .about-text { position: absolute; left: 421px; top: 603px; width: 465px; font-size: 14.2px; line-height: 15.6px; }
  .about-text p + p { margin-top: 15px; }
  .reasons-title {
    position: absolute; left: 155px; top: 792px;
    font-family: "Oxygen", sans-serif; font-size: 25px; letter-spacing: 1px;
  }
  .reason { position: absolute; left: 164px; width: 440px; }
  .reason h3 {
    font-family: "Oxygen", sans-serif; font-weight: 700; font-size: 15.5px;
    display: flex; align-items: center; gap: 9px;
  }
  .reason p { margin-left: 26px; margin-top: 3px; font-size: 10.6px; line-height: 12px; font-weight: 600; }
  .quote-panel {
    position: absolute; left: 671px; top: 752px; width: 251px; height: 420px;
    background: var(--panel-navy);
  }
  .quote-title {
    position: absolute; left: 0; width: 251px; top: 32px; text-align: center;
    font-family: "Oswald", sans-serif; font-weight: 500; font-size: 24px;
  }
  .field {
    position: absolute; left: 18px; width: 211px; height: 30px;
    border: 3px solid var(--field-border); background: transparent;
    color: var(--field-text); font-size: 12px; padding: 6px 8px;
  }
  .field-comment { height: 66px; }
  .submit {
    position: absolute; left: 18px; top: 372px; width: 211px; height: 32px;
    background: var(--header-blue); text-align: center; line-height: 32px;
    font-family: "Oswald", sans-serif; font-weight: 500; font-size: 17px;
  }
  .page-foot { position: absolute; left: 0; top: 1194px; width: 1080px; height: 6px; background: var(--header-blue); }
</style>
</head>
<body>
  <header class="site-header">
    <div class="brand"><span class="brand-mark"></span>Bluefinch Painting</div>
    <nav class="main-nav">
      <a class="is-active" href="#about">About</a>
      <a href="#service">Service</a>
      <a href="#projects">Projects</a>
      <a href="#contact">Contact Us</a>
    </nav>
  </header>

  <section class="hero" role="img" aria-label="Photo of a house with a company pickup truck and two work trailers parked in front">
    <h1 class="hero-title">Welcome to Bluefinch Painting</h1>
    <p class="hero-lead">Lorem Ipsum is simply dummy text of the printing and typesetting industry. Lorem Ipsum has been the industry's standard dummy text ever since the 1500s, when an unknown printer took a galley</p>
    <svg class="hero-scroll" width="24" height="14" viewBox="0 0 24 14"><path d="M2 2 L12 11 L22 2" fill="none" stroke="#fff" stroke-width="3"/></svg>
  </section>

  <h2 class="section-title" id="about">About Us</h2>
  <div class="section-rule"></div>
  <div class="about-photo" role="img" aria-label="Photo of a company work trailer parked in front of a house"></div>
  <div class="about-text">
    <p>Vestibulum pede. Maecenas sit amet augue. Sed blandit lect us eget lectus. Mauris justo. Curabitur nibh lectus, dapibus id, tempor eu, tempor non, erat. Proin pede eros, pharetra ut, viverra sed, egestas nec, mauris.</p>
    <p>Nulla tempor fermentum orci. Maecenas ac est hendrerit magna ali-quam sagittis. Curabitur convallis interdum erat. Proin feugiat sem eu nisl. Aliquam erat volutpat. Fusce a mauris vel nulla faucibus tempor.</p>
  </div>

  <h2 class="reasons-title">Why You Should Choose Us</h2>
  <div class="reason" style="top:843px">
    <h3><svg width="16" height="12" viewBox="0 0 16 12"><path d="M1 1 L6 6 L1 11 M8 1 L13 6 L8 11" fill="none" stroke="#fff" stroke-width="2.4"/></svg>Lorem ipsum dolor sit amet, consectetur</h3>
    <p>Lorem ipsum dolor sit amet, consectetur adipiscing elit. Sed blandit massa vel mauris sollicitudin dignissim. Phasellus ultrices tellus eget ipsum ornare molestie scelerisque eros</p>
  </div>
  <div class="reason" style="top:926px">
    <h3><svg width="16" height="12" viewBox="0 0 16 12"><path d="M1 1 L6 6 L1 11 M8 1 L13 6 L8 11" fill="none" stroke="#fff" stroke-width="2.4"/></svg>Lorem ipsum dolor sit amet, consectetur</h3>
    <p>Lorem ipsum dolor sit amet, consectetur adipiscing elit. Sed blandit massa vel mauris sollicitudin dignissim. Phasellus ultrices tellus eget ipsum ornare molestie scelerisque eros dignissim. Phasellus</p>
  </div>
  <div class="reason" style="top:1009px">
    <h3><svg width="16" height="12" viewBox="0 0 16 12"><path d="M1 1 L6 6 L1 11 M8 1 L13 6 L8 11" fill="none" stroke="#fff" stroke-width="2.4"/></svg>Lorem ipsum dolor sit amet, consectetur</h3>
    <p>Lorem ipsum dolor sit amet, consectetur adipiscing elit. Sed blandit massa vel mauris sollicitudin dignissim. Phasellus ultrices tellus eget ipsum ornare molestie scelerisque eros dignissim.</p>
  </div>
  <div class="reason" style="top:1090px">
    <h3><svg width="16" height="12" viewBox="0 0 16 12"><path d="M1 1 L6 6 L1 11 M8 1 L13 6 L8 11" fill="none" stroke="#fff" stroke-width="2.4"/></svg>Lorem ipsum dolor sit amet, consectetur</h3>
    <p>Lorem ipsum dolor sit amet, consectetur adipiscing elit. Sed blandit massa vel mauris sollicitudin dignissim. Phasellus ultrices tellus eget ipsum ornare molestie scelerisque</p>
  </div>

  <aside class="quote-panel" id="contact">
    <h2 class="quote-title">Request Free Quote</h2>
    <div class="field" style="top:86px">Your Name</div>
    <div class="field" style="top:137px">Your Email</div>
    <div class="field" style="top:189px">Phone</div>
    <div class="field" style="top:240px">City</div>
    <div class="field field-comment" style="top:290px">Comment</div>
    <div class="submit">Submit</div>
  </aside>

  <div class="page-foot"></div>
</body>
</html>
```